A Speech Therapy Business needs to update their logo

I need an update to the font and color of my logo to look more appealing. I am looking to open a private practice as a Speech Language Pathologist that caters to adults and children. It needs to be sophisticated and friendly at the same time. I want to keep the silhouette in my logo as is, just update the font and color for "Brightpaths".
Industry/Entity Type
Business
Contact Information for Business Card
I want the business card to have my logo, my name (Dorota Valk, CCC-SLP, TSSLD) and that I am a Bilingual Speech Language Pathologist. Also, include my phone number, (555) 271-8390. Include my website, Brightpathsslp.example, and email address, dorotavalk@brightpathsslp.example
Look and feel
Each slider illustrates characteristics of the customer's brand and the style your logo design should communicate.

```html
<!DOCTYPE html>
<html lang="en">
<head>
<meta charset="utf-8">
<title>Brightpaths – Business Card</title>
<link rel="stylesheet" href="https://fonts.googleapis.com/css2?family=Open+Sans:wght@300;400&display=swap">
<style>
  :root {
    --page-bg: #ffffff;
    --card-bg: #f7f7f7;
    --card-edge: #e4e4e4;
    --ink-dark: #1c1c1c;
    --ink-muted: #7a7a7a;
    --brand-red: #973631;
    --contact-red: #b5524a;
  }
  * { margin: 0; padding: 0; box-sizing: border-box; }
  html, body {
    width: 1200px;
    height: 848px;
    overflow: hidden;
    background: var(--page-bg);
    font-family: "Open Sans", Arial, sans-serif;
  }
  .business-card {
    position: absolute;
    left: 268px;
    top: 239px;
    width: 666px;
    height: 371px;
    border-radius: 17px;
    background: var(--card-bg);
    border: 1px solid var(--card-edge);
  }
  .job-title {
    position: absolute;
    left: 54px;
    top: 64px;
    font-size: 15px;
    font-weight: 400;
    line-height: 19px;
    letter-spacing: 0.4px;
    color: var(--ink-muted);
  }
  .brand-mark {
    position: absolute;
    right: 50px;
    top: 44px;
    display: flex;
    align-items: center;
    gap: 10px;
  }
  .brand-dot {
    width: 14px;
    height: 14px;
    border-radius: 50%;
    background: var(--brand-red);
  }
  .brand-name {
    font-size: 30px;
    font-weight: 400;
    letter-spacing: 1px;
    color: var(--brand-red);
  }
  .person {
    position: absolute;
    left: 54px;
    top: 248px;
  }
  .person-name {
    font-size: 37px;
    font-weight: 300;
    line-height: 44px;
    color: var(--ink-dark);
    text-transform: uppercase;
  }
  .person-credentials {
    font-size: 13px;
    font-weight: 400;
    line-height: 16px;
    color: var(--ink-muted);
  }
  .contact-list {
    position: absolute;
    right: 53px;
    top: 256px;
    list-style: none;
    text-align: right;
    font-size: 15px;
    font-weight: 400;
    line-height: 18.5px;
    color: var(--contact-red);
  }
</style>
</head>
<body>
  <section class="business-card">
    <p class="job-title">Bilingual Speech Language<br>Pathologist</p>

    <div class="brand-mark">
      <span class="brand-dot"></span>
      <span class="brand-name">Brightpaths</span>
    </div>

    <div class="person">
      <h1 class="person-name">Dorota Valk</h1>
      <p class="person-credentials">CCC-SLP, TSSLD</p>
    </div>

    <ul class="contact-list">
      <li class="contact-phone">+1.555.271.83.90</li>
      <li class="contact-web">www.brightpathsslp.example</li>
      <li class="contact-email">dorotavalk@brightpathsslp.example</li>
    </ul>
  </section>
</body>
</html>
```